Veltro Metrics New Website for Health Benefits Plan Decisioneering Tool Launch

Veltro Metrics is a SaaS provider of health benefits comparison tools. We need a new simple SaaS focused website to direct customers to our product

Target Market(s)

General Public comparing their health benefits plans from their employer or from the state exchanges in the US

Coding

Coded - Design and coding required

Number of Pages Required

3 page

Requirements
Must have
• Main page - "Know the Best Health Benefits Plan for You!"
Graphic of a person looking over papers on their desk
Compare Now button to link to SaaS product
About Us
Product Page

https://plimquo.example/top-saas-sites/

```html
<!DOCTYPE html>
<html lang="en">
<head>
<meta charset="UTF-8">
<title>Veltro Metrics – Know the Best Health Benefits Plan for You</title>
<link rel="stylesheet" href="https://fonts.googleapis.com/css2?family=Cinzel:wght@500;600&family=Mulish:wght@400;500;600&display=swap">
<style>
  :root {
    --sky: #e4effe;
    --brand: #29abe2;
    --brand-deep: #219fd8;
    --ink: #111111;
    --white: #ffffff;
    --art-light: #eef4fd;
    --art-mid: #cfe0f6;
    --art-deep: #a9c6ec;
  }
  * { margin: 0; padding: 0; box-sizing: border-box; }
  html, body { width: 1200px; height: 1004px; overflow: hidden; }
  body {
    position: relative;
    background: var(--white);
    font-family: "Mulish", sans-serif;
    color: var(--ink);
  }
  .hero {
    position: absolute; left: 0; top: 0;
    width: 1200px; height: 650px;
    background: var(--sky);
  }
  .site-header {
    position: absolute; left: 161px; top: 26px;
    width: 878px; height: 72px;
    display: flex; align-items: center; justify-content: space-between;
    z-index: 2;
  }
  .brand-name {
    font-family: "Cinzel", serif;
    font-weight: 500;
    font-size: 30px;
    letter-spacing: 0.5px;
    color: var(--brand);
    text-transform: uppercase;
  }
  .main-nav { display: flex; gap: 39px; margin-top: -24px; }
  .main-nav a {
    font-size: 13.5px; font-weight: 500;
    color: var(--ink); text-decoration: none;
    letter-spacing: 0.2px;
  }
  .hero-art {
    position: absolute; left: 443px; top: 109px;
    width: 757px; height: 541px;
    background: radial-gradient(ellipse at 65% 60%, var(--art-mid) 0%, var(--art-light) 55%, var(--sky) 85%);
  }
  .hero-copy {
    position: absolute; left: 163px; top: 220px;
    z-index: 2;
  }
  .hero-title {
    font-family: "Cinzel", serif;
    font-weight: 600;
    font-size: 40px;
    line-height: 51px;
    color: var(--brand);
  }
  .btn {
    display: inline-flex; align-items: center; justify-content: center;
    background: var(--brand);
    color: var(--white);
    font-family: "Mulish", sans-serif;
    font-weight: 600;
    text-decoration: none;
    border-radius: 30px;
    letter-spacing: 0.3px;
  }
  .btn-compare {
    position: absolute; left: 161px; top: 391px;
    width: 188px; height: 45px; font-size: 15px;
    z-index: 2;
  }
  .about-card {
    position: absolute; left: 161px; top: 604px;
    width: 878px; height: 293px;
    background: var(--white);
    border-radius: 12px;
    box-shadow: 0 4px 12px rgba(40, 70, 110, 0.12);
    text-align: center;
    z-index: 3;
  }
  .about-title {
    font-family: "Cinzel", serif;
    font-weight: 600;
    font-size: 34px;
    color: var(--brand);
    margin-top: 60px;
    line-height: 44px;
  }
  .about-text {
    width: 820px; margin: 14px auto 0;
    font-size: 13.5px; line-height: 24.5px;
  }
  .btn-more {
    margin-top: 16px;
    width: 172px; height: 37px; font-size: 14.5px;
  }
  .site-footer {
    position: absolute; left: 0; top: 959px;
    width: 1200px; height: 45px;
    background: var(--brand);
    color: var(--white);
    font-size: 13px;
    display: flex; align-items: center; justify-content: center;
  }
</style>
</head>
<body>
  <section class="hero">
    <div class="hero-art" role="img" aria-label="Illustration of a smiling man at his desk holding a pen, reviewing papers beside a laptop"></div>
  </section>

  <header class="site-header">
    <div class="brand-name">Veltro Metrics</div>
    <nav class="main-nav">
      <a href="#">HOME</a>
      <a href="#">ABOUT US</a>
      <a href="#">PRODUCT PAGE</a>
    </nav>
  </header>

  <div class="hero-copy">
    <h1 class="hero-title">Know the Best<br>Health Benefits<br>Plan for You!</h1>
  </div>
  <a class="btn btn-compare" href="https://plimquo.example/top-saas-sites/">COMPARE NOW</a>

  <section class="about-card">
    <h2 class="about-title">ABOUT US</h2>
    <p class="about-text">Lorem ipsum dolor sit amet, consectetuer adipiscing elit, sed diam nonummy nibh euismod tincidunt ut laoreet dolore magna aliquam erat volutpat. Ut wisi enim ad minim veniam, quis nostrud exerci tation ullamcorper suscipit lobortis nisl ut aliquip ex ea commodo consequat. Duis autem vel eum iriure dolor in hendrerit in vulputate velit esse molestie consequat.</p>
    <a class="btn btn-more" href="#">KNOW MORE</a>
  </section>

  <footer class="site-footer">Copyright © 2020 VELTRO METRICS. All Rights Reserved.</footer>
</body>
</html>
```